Redesign of Real Estate Agency Website

We need a redesign for our real estate agency website. Please see attached creative brief.

Target Market(s)

Refer to creative brief.

Industry/Entity Type

Real Estate

Requirements
Must have
• Refer to creative brief.

```html
<!DOCTYPE html>
<html lang="en">
<head>
<meta charset="utf-8">
<title>Coralbay.net – Magnificent Sea View Villa</title>
<link rel="stylesheet" href="https://fonts.googleapis.com/css2?family=Arimo:wght@400;700&family=Open+Sans:wght@400;600&family=Roboto+Condensed:wght@400;700&display=swap">
<style>
:root{
  --page:#ffffff;
  --ink:#1e1e1e;
  --muted:#6b6b6b;
  --nav:#666666;
  --cyan:#19c8d6;
  --title-gray:#8a9aa3;
  --band-top:#000000;
  --band-bottom:#0c5f86;
  --side:#0b2c3f;
  --pill:#e0e0e0;
  --pill-border:#b9b9b9;
  --footer-top:#6f6f6f;
  --footer-bottom:#8c8c8c;
  --footer-text:#e8e8e8;
  --footer-dim:#b0b0b0;
}
*{box-sizing:border-box;margin:0;padding:0}
html,body{width:1200px;height:900px;overflow:hidden;background:var(--page)}
body{position:relative;font-family:"Arimo",Arial,sans-serif;color:var(--ink)}
.abs{position:absolute}
.sheet{left:78px;top:6px;width:1040px;height:894px;background:var(--page);box-shadow:0 0 8px rgba(0,0,0,.35)}
.band{left:0;top:105px;width:1200px;height:278px;background:linear-gradient(180deg,var(--band-top) 0%,#04263a 45%,var(--band-bottom) 100%)}
.sidebar{left:90px;top:105px;width:216px;height:278px;background:linear-gradient(180deg,#050d13,var(--side))}
.brand{left:96px;top:56px;font-family:"Open Sans",sans-serif;font-size:31px;letter-spacing:5px;color:#6a6a6a;display:flex;align-items:center;gap:8px}
.brand-dot{width:14px;height:14px;border-radius:50%;background:#6fb82c;position:absolute;left:70px;top:-16px}
.cart{left:1015px;top:16px;width:92px;height:22px;border-radius:11px;background:#e4e4e4;font-family:"Open Sans",sans-serif;font-size:12px;color:#555;text-align:center;line-height:22px}
.nav{top:64px;left:348px;display:flex;font-family:"Open Sans",sans-serif;font-size:14px;color:var(--nav)}
.nav a{color:inherit;text-decoration:none;height:32px;line-height:32px;padding:0 13px}
.nav a.active{background:#dcdcdc;border-radius:8px;padding:0 15px}
.qs-title{left:107px;top:125px;font-family:"Open Sans",sans-serif;font-size:13px;font-weight:600;color:#fff}
.qs-title b{color:var(--cyan);font-weight:600}
.select{left:106px;width:187px;height:23px;background:linear-gradient(#fff,#e9e9e9);border-radius:4px;font-family:"Open Sans",sans-serif;font-size:12px;color:#555;line-height:23px;padding-left:11px}
.select::after{content:"";position:absolute;right:0;top:0;width:22px;height:23px;background:#c9c9c9;border-radius:0 4px 4px 0}
.select i{position:absolute;right:6px;top:9px;width:0;height:0;border-left:5px solid transparent;border-right:5px solid transparent;border-top:6px solid #fff;z-index:1}
.side-link{left:112px;font-family:"Open Sans",sans-serif;font-size:12px;color:#9bb6c6;text-decoration:underline}
.btn-search{left:215px;top:337px;width:71px;height:25px;border-radius:13px;background:linear-gradient(#fff,#cfcfcf);font-family:"Open Sans",sans-serif;font-size:12px;color:#444;text-align:center;line-height:25px}
.back{left:1081px;top:112px;font-size:10px;color:#ccc;text-decoration:underline}
.title{left:345px;top:121px;font-family:"Roboto Condensed",sans-serif;font-size:18px;font-weight:700;color:var(--cyan);letter-spacing:.3px}
.title span{color:var(--title-gray);font-weight:400}
.hero{left:342px;top:161px;width:451px;height:284px;border:3px solid #fff;box-shadow:0 4px 10px rgba(0,0,0,.5);background:linear-gradient(180deg,#3b8fd6 0%,#8ec3ec 45%,#3fb2c2 58%,#a8b59a 80%,#b7a58a 100%)}
.thumb{width:88px;height:58px;border:2px solid #fff;box-shadow:2px 3px 5px rgba(0,0,0,.5)}
.thumb.warm{background:linear-gradient(160deg,#5a2a0c,#c0782c 55%,#e3c89a)}
.thumb.pool{background:linear-gradient(180deg,#4e9ad6,#8fc4e6 45%,#2f6f8c 70%,#1e2f3b)}
.pill{height:25px;border-radius:13px;background:linear-gradient(#f2f2f2,#d8d8d8);border:1px solid var(--pill-border);font-family:"Open Sans",sans-serif;font-size:12px;color:#555;text-align:center;line-height:23px}
h2{position:absolute;font-family:"Arimo",Arial,sans-serif;font-weight:400;font-size:14px;color:var(--cyan)}
.copy{font-size:12px;line-height:15px;color:var(--ink)}
.facts{left:818px;font-size:12px;line-height:15px}
.facts div{display:flex;height:16px}
.facts dt{width:144px;font-weight:700;color:#333}
.facts dd{color:#333}
.facts .price{font-weight:700}
.view-map{left:816px;top:744px;font-size:12px;color:#555;text-decoration:underline}
.browse{left:346px;top:774px;font-family:"Open Sans",sans-serif;font-size:12px;color:#555;display:flex;gap:11px}
.browse b{font-weight:600;color:#444}
.sitemap{left:1036px;top:791px;width:65px;height:16px;background:#cfcfcf;border-radius:3px;font-size:10px;color:#444;text-align:center;line-height:16px}
.footer{left:78px;top:806px;width:1040px;height:94px;background:linear-gradient(180deg,var(--footer-top),var(--footer-bottom))}
.foot-nav{left:111px;top:824px;font-size:10px;color:var(--footer-text)}
.foot-line{left:111px;font-size:10px;color:var(--footer-dim)}
.emblem{left:988px;top:806px;width:113px;height:94px;background:linear-gradient(180deg,rgba(255,255,255,.08),rgba(255,255,255,.16))}
</style>
</head>
<body>
<div class="abs sheet"></div>
<div class="abs band"></div>
<div class="abs sidebar"></div>

<div class="abs brand"><span class="brand-dot"></span>CORALBAY</div>
<div class="abs cart">cart is empty</div>
<nav class="abs nav">
  <a href="#">HOME</a>
  <a href="#" class="active">FOR SALE</a>
  <a href="#">FOR RENT</a>
  <a href="#">CONTACT US</a>
  <a href="#" style="margin-left:14px">ABOUT US</a>
  <a href="#">LIST YOUR PROPERTY</a>
  <a href="#" style="margin-left:14px">BUYER'S GUIDE</a>
</nav>

<div class="abs qs-title"><b>QUICK</b> SEARCH</div>
<div class="abs select" style="top:151px">Buy Property<i></i></div>
<div class="abs select" style="top:180px">Property Type<i></i></div>
<div class="abs select" style="top:209px">Region<i></i></div>
<div class="abs select" style="top:237px">District<i></i></div>
<div class="abs select" style="top:266px">Minimum Bedrooms<i></i></div>
<div class="abs select" style="top:295px">Maximum Price THB<i></i></div>
<a class="abs side-link" style="top:331px">Advanced search</a>
<a class="abs side-link" style="top:348px">Search by map</a>
<div class="abs btn-search">search</div>

<a class="abs back">Back</a>
<div class="abs title">MAGNIFICENT <span>SEA VIEW VILLA</span></div>
<div class="abs hero" role="img" aria-label="Villa terrace with sun loungers and parasols beside an infinity pool overlooking the bay"></div>

<div class="abs thumb warm" style="left:840px;top:162px" role="img" aria-label="Villa living room"></div>
<div class="abs thumb pool" style="left:948px;top:162px" role="img" aria-label="Pool terrace"></div>
<div class="abs thumb warm" style="left:840px;top:238px" role="img" aria-label="Lounge with sea view"></div>
<div class="abs thumb pool" style="left:949px;top:238px" role="img" aria-label="Sea view from terrace"></div>
<div class="abs thumb pool" style="left:841px;top:309px" role="img" aria-label="Pool at dusk"></div>
<div class="abs thumb warm" style="left:950px;top:309px" role="img" aria-label="Living area at night"></div>

<div class="abs pill" style="left:830px;top:408px;width:131px">Add to inquiry cart</div>
<div class="abs pill" style="left:968px;top:408px;width:78px">Inquire</div>

<h2 style="left:345px;top:464px">Description</h2>
<p class="abs copy" style="left:346px;top:479px;width:440px">Vista Park looks further into condominium unit design by offering a smart duplex layout that gives the resident an enhanced feeling of space within their living environment.</p>
<p class="abs copy" style="left:346px;top:535px;width:440px">The duplex design allows for large windows which maximise light and view and also create an eye-catching appearance from the exterior. Our smart design goes even further by offering residents private access from the elevators direct into their own private corridor, which also acts as an excellent security feature.</p>

<h2 style="left:346px;top:613px">Inquire About this Property</h2>
<p class="abs copy" style="left:346px;top:630px;width:430px">To request more information about this property, please provide us with your email address, name and any questions that you might have. We will respond within 24 hours.</p>
<p class="abs copy" style="left:346px;top:674px">We look forward to assisting you.</p>
<p class="abs copy" style="left:346px;top:704px;width:440px">To submit an inquiry for multiple properties click “Add to Inquiry Cart”. You will be taken the Inquiry Cart page where you can review items and then continue to inquiry form or add more properties.</p>

<h2 style="left:818px;top:464px">Fact Sheet</h2>
<dl class="abs facts" style="top:480px">
  <div><dt>Price</dt><dd class="price">USD 5.95M</dd></div>
  <div><dt>Type</dt><dd>Villa</dd></div>
  <div><dt>Location</dt><dd>Kamala, West Phuket</dd></div>
  <div><dt>View</dt><dd>Sea View</dd></div>
  <div><dt>Reference no.</dt><dd>1583</dd></div>
</dl>
<h2 style="left:818px;top:571px">Property Details</h2>
<dl class="abs facts" style="top:589px">
  <div><dt>Land Area</dt><dd>2313 sqm</dd></div>
  <div><dt>Built-up Area</dt><dd>786 sqm</dd></div>
  <div><dt>Bedrooms</dt><dd>6</dd></div>
  <div><dt>Bathrooms</dt><dd>6</dd></div>
  <div style="margin-top:1px"><dt>Swimming Pool</dt><dd>Private</dd></div>
  <div><dt>Jacuzzi</dt><dd>Outdoor</dd></div>
  <div><dt>Car Parking</dt><dd>Shared</dd></div>
  <div style="margin-top:1px"><dt>Furnished</dt><dd>Fully-furnished</dd></div>
  <div><dt>Ownership Structure</dt><dd>Leasehold</dd></div>
</dl>
<a class="abs view-map">View Map</a>

<div class="abs browse"><b>Browse Properties:</b><span>Apartments and Condos</span><span>Villas and Houses</span><span>Commercial</span><span>Lands</span></div>

<div class="abs footer"></div>
<div class="abs emblem" role="img" aria-label="Faint heraldic crest decoration"></div>
<div class="abs sitemap">View sitemap</div>
<div class="abs foot-nav">Home | For Sale | For Rent | Contact Us | About Us | List your property | Buyer's guide</div>
<div class="abs foot-line" style="top:837px">Phuket Property and Real Estate for Sale</div>
<div class="abs foot-line" style="top:852px">Copyright © Coralbay.Net 2008-2010</div>
<div class="abs foot-line" style="top:864px">All Rights Reserved</div>
</body>
</html>
```